Web page design/layout for dog breeder

We are looking for a new layout/design for our current web page. Current web pages can be found at http://rustpointer.hostlark.net.

We recently uploaded the NTG Kennel of Distinction banner that we would like to have displayed on the home page.

```html
<!DOCTYPE html>
<html lang="en">
<head>
<meta charset="utf-8">
<title>Rustpoint Pointers</title>
<link rel="stylesheet" href="https://fonts.googleapis.com/css2?family=Arimo:wght@400;700&display=swap">
<style>
:root{
  --dark:#2f2f2f;
  --light-bg:#e4e4e4;
  --panel:#f1f1f3;
  --panel-line:#cfcfd3;
  --green:#3f5d1e;
  --green-dark:#2b4212;
  --olive:#4d4a2a;
  --orange:#f07b12;
  --logo-green:#4a6a1c;
  --badge:#b8962e;
  --text:#333;
  --link:#2a6fa8;
  --red:#c51818;
  --footer:#4c4c4c;
  --footer-head:#333;
}
*{box-sizing:border-box;margin:0;padding:0}
html,body{width:1050px;height:1200px;overflow:hidden}
body{position:relative;font-family:"Arimo",Arial,sans-serif;color:var(--text);background:var(--light-bg)}
.abs{position:absolute}
.top-band{left:0;top:0;width:1050px;height:384px;background:linear-gradient(90deg,#262626,#3b3b3b 20%,#3b3b3b 80%,#262626)}
.logo-tab{left:152px;top:0;width:264px;height:87px;background:linear-gradient(#fff,#e9e9e9);border-radius:0 0 18px 18px;box-shadow:0 2px 6px rgba(0,0,0,.5)}
.logo-name{position:absolute;left:18px;top:30px;font-size:25px;font-weight:700;color:var(--logo-green);letter-spacing:-.5px;white-space:nowrap}
.award-banner{left:436px;top:46px;width:140px;height:38px;background:linear-gradient(#d4b24a,var(--badge));border-radius:4px}
.contact-pill{left:497px;top:7px;width:381px;height:25px;background:linear-gradient(#fafafa,#dcdcdc);border-radius:13px;font-size:11px;color:#333;display:flex;align-items:center;gap:26px;padding-left:16px;white-space:nowrap}
.contact-pill span{display:flex;align-items:center;gap:8px}
.search{left:738px;top:59px;width:147px;height:23px;background:#fff;border-radius:12px;font-size:10px;font-style:italic;color:#555;padding:6px 10px}
.search svg{position:absolute;right:6px;top:3px}
.page{left:141px;top:99px;width:769px;height:869px;background:#fff;border-radius:10px;box-shadow:0 0 6px rgba(0,0,0,.45)}
.nav{left:160px;top:102px;width:729px;height:35px;background:linear-gradient(#4d7026,var(--green-dark));border-radius:0 0 12px 12px;display:flex;align-items:center;padding:0 6px}
.nav a{flex:auto;text-align:center;white-space:nowrap;color:#fff;text-decoration:none;font-size:11.5px;padding:0 5px;border-left:1px solid #5f8436;line-height:35px}
.nav a:first-child{border-left:none}
.slider{left:152px;top:151px;width:507px;height:271px;border:3px solid #ddd;background:linear-gradient(160deg,#8c7553,#6a5236 45%,#a58d66);overflow:hidden}
.slider .cap{position:absolute;left:28px;top:215px;color:#fff;font-size:17px;text-shadow:0 1px 2px #000;white-space:nowrap}
.slider .dots{position:absolute;right:12px;bottom:8px;display:flex;gap:4px}
.slider .dots i{width:8px;height:8px;background:#fff;display:block}
.slider .dots i:first-child{background:var(--red)}
.slide-arrows{left:391px;top:430px;display:flex;gap:3px}
.slide-arrows i{width:16px;height:20px;background:#bbb;color:#fff;font-style:normal;font-size:13px;text-align:center;line-height:20px}
.box-head{background:linear-gradient(#5d5a36,var(--olive));color:#fff;font-size:12px;padding-left:12px}
.contact-box{left:672px;top:150px;width:225px;height:273px;background:var(--panel);border:1px solid var(--panel-line)}
.contact-box .box-head{height:30px;line-height:30px;font-size:13px}
.field{position:absolute;left:10px;font-size:11px;color:#333}
.input{position:absolute;left:66px;width:148px;height:18px;background:#fff;border:1px solid #bbb;border-radius:2px}
.btn{background:linear-gradient(#4c6d28,var(--green-dark));color:#fff;font-size:10px;text-align:center;border-radius:3px;white-space:nowrap}
.info{top:463px;width:243px;height:137px;background:var(--panel);border:1px solid var(--panel-line);border-radius:4px}
.info h3{font-weight:400;font-size:13px;text-align:center;margin-top:11px;color:#333}
.info .photo{position:absolute;left:9px;top:40px;width:76px;height:76px}
.info p{position:absolute;left:92px;top:43px;width:140px;font-size:8.5px;line-height:11px;color:#444}
.info .btn{position:absolute;right:11px;bottom:11px;width:72px;height:18px;line-height:18px}
.welcome{left:168px;top:625px;width:470px}
.welcome h1{font-weight:400;font-size:22px;color:#333;white-space:nowrap}
.welcome h1 b{font-weight:400;color:var(--green)}
.welcome p{font-size:10.5px;line-height:14px;color:#333;margin-top:10px}
.read-more{left:556px;top:818px;width:72px;height:21px;line-height:21px;font-size:10px;border-radius:6px}
.testimonials{left:152px;top:849px;width:511px;height:106px;background:var(--panel);border:1px solid var(--panel-line)}
.testimonials .box-head{height:26px;line-height:26px;position:relative}
.testimonials .box-head span{position:absolute;right:14px;top:0;font-size:16px}
.testimonials .avatar{position:absolute;left:20px;top:42px;width:44px;height:46px}
.testimonials p{position:absolute;left:96px;top:38px;width:400px;font-size:11px;line-height:14px;color:#333}
.testimonials .who{position:absolute;left:96px;top:86px;font-size:8px;color:#444}
.testimonials .who b{color:var(--red);font-weight:400}
.news{left:672px;top:617px;width:227px;height:338px;background:var(--panel);border:1px solid var(--panel-line)}
.news .box-head{height:26px;line-height:26px}
.news ul{list-style:none}
.news li{position:relative;height:41px;border-bottom:1px solid #d6d6d6}
.news li i{position:absolute;left:11px;top:8px;width:27px;height:27px}
.news li span{position:absolute;left:54px;top:8px;width:166px;font-size:9px;line-height:12px;color:#444}
.news li span b{font-weight:400;color:var(--link)}
.news .all{position:absolute;right:8px;bottom:7px;font-size:9px;color:var(--red);text-decoration:underline}
.footer{left:0;top:978px;width:1050px;height:197px;background:var(--footer)}
.footer-head{left:0;top:978px;width:1050px;height:34px;background:var(--footer-head)}
.fcol{top:986px;color:#eee;font-size:10px;white-space:nowrap}
.fcol h4{font-weight:400;font-size:11px;color:#fff;height:32px}
.fcol li{list-style:none;line-height:16.5px}
.address{line-height:12px}
.address td{padding:0 4px 0 0}
.social li{display:flex;align-items:center;gap:8px;line-height:20px;font-weight:700}
.social li i{width:15px;height:15px;background:#2f6fae;display:block}
.social li:last-child i{background:var(--orange)}
.newsletter{left:672px;top:1034px;width:227px;height:119px;background:#fff;border-radius:4px}
.newsletter .box-head{height:27px;line-height:27px;font-size:13px}
.newsletter p{font-size:10px;color:#555;margin:8px 12px 0;line-height:12px}
.newsletter .email{position:absolute;left:11px;top:69px;width:144px;height:22px;border:1px solid #bbb;border-radius:3px;font-size:8.5px;color:#444;padding:5px}
.newsletter .btn{position:absolute;left:160px;top:69px;width:55px;height:22px;line-height:22px;font-size:11px}
.newsletter .agree{position:absolute;left:11px;top:99px;font-size:8px;color:#444;display:flex;align-items:center;gap:6px}
.newsletter .agree i{width:11px;height:11px;border:1px solid #999;display:block}
.copyright{left:0;top:1175px;width:1050px;height:25px;background:#111;color:#fff;font-size:11px;text-align:center;line-height:25px}
</style>
</head>
<body>
<div class="abs top-band"></div>

<div class="abs logo-tab"><div class="logo-name">Rustpoint Pointers</div></div>

<div class="abs award-banner" role="img" aria-label="NTG Kennel of Distinction banner"></div>

<div class="abs contact-pill">
  <span><svg width="14" height="12" viewBox="0 0 14 12"><path d="M1 3c0-2 2-2 2-2h8s2 0 2 2v1h-3V3H4v1H1z M3 5h8l2 6H1z" fill="#666"/></svg>Phone : 555 -010 -4420</span>
  <span><svg width="14" height="10" viewBox="0 0 14 10"><rect x=".5" y=".5" width="13" height="9" fill="none" stroke="#666"/><path d="M.5.5l6.5 5 6.5-5" fill="none" stroke="#666"/></svg>e-mail : rp1972@mailbox.test</span>
</div>

<div class="abs search">Search
  <svg width="18" height="17" viewBox="0 0 18 17"><circle cx="7" cy="7" r="5" fill="none" stroke="#222" stroke-width="2"/><path d="M11 11l5 5" stroke="#222" stroke-width="3"/></svg>
</div>

<div class="abs page"></div>

<nav class="abs nav">
  <a>HOME</a><a>OUR DOGS</a><a>UPCOMING LITTERS</a><a>GALLERIES</a><a>ABOUT</a><a>TESTIMONIALS</a><a>BLOG</a><a>PAST LITTERS</a><a>CONTACT US</a>
</nav>

<div class="abs slider" role="img" aria-label="Pointer dog in an orange vest hunting in dry field grass">
  <div class="cap">Lorem Ipsum dolor Sit Amet, consecteteur adipiscing elit.</div>
  <div class="dots"><i></i><i></i><i></i><i></i></div>
</div>
<div class="abs slide-arrows"><i>&#8249;</i><i>&#8250;</i></div>

<div class="abs contact-box">
  <div class="box-head">CONTACT US</div>
  <div class="field" style="top:57px">Name</div><div class="input" style="top:53px"></div>
  <div class="field" style="top:77px">Email</div><div class="input" style="top:74px"></div>
  <div class="field" style="top:98px">Phone</div><div class="input" style="top:95px"></div>
  <div class="field" style="top:119px">Message</div><div class="input" style="top:117px;height:110px"></div>
  <div class="btn abs" style="left:151px;top:233px;width:63px;height:22px;line-height:22px">SUBMIT</div>
</div>

<div class="abs info" style="left:152px">
  <h3>WHO WE ARE</h3>
  <div class="photo" role="img" aria-label="Two hunters in orange gear with their dogs" style="background:linear-gradient(#8a7a5e,#c36a22 60%,#5a4a33)"></div>
  <p>Lorem ipsum dolor sit amet, con secteteur adipiscing elit. Set diem nonumy, in convalis gravida neq ue. Nulla gravida vestibulum ne tis a acumsan</p>
  <div class="btn">read more &gt;&gt;</div>
</div>
<div class="abs info" style="left:405px">
  <h3>WHAT WE DO</h3>
  <div class="photo" role="img" aria-label="Handler kneeling with a pointer dog in a field" style="background:linear-gradient(#9fb0a0,#b89a73 55%,#7a5a3a)"></div>
  <p>Lorem ipsum dolor sit amet, con secteteur adipiscing elit. Set diem nonumy, in convalis gravida neq ue. Nulla gravida vestibulum ne tis a acumsan</p>
  <div class="btn">read more &gt;&gt;</div>
</div>
<div class="abs info" style="left:656px">
  <h3>OUR SERVICES</h3>
  <div class="photo" role="img" aria-label="Litter of red puppies sitting together" style="background:linear-gradient(#c9c2b6,#b06a3a 55%,#8a4e2a)"></div>
  <p>Lorem ipsum dolor sit amet, con secteteur adipiscing elit. Set diem nonumy, in convalis gravida neq ue. Nulla gravida vestibulum ne tis a acumsan</p>
  <div class="btn">read more &gt;&gt;</div>
</div>

<section class="abs welcome">
  <h1>Welcome To <b>Rustpoint Pointers</b></h1>
  <p>&nbsp;&nbsp;&nbsp;&nbsp;&nbsp;We were introduced to our first pointer on hunting trip in the mind 1990's. we were impressed by this medium sized dog that had a superior nose and high class hunting ability. And so it began, our first pointer , Max, joinde our familyin 1999.</p>
  <p>Our pointers have always been a part of our family and spend many hours eaech year in the field with us as our hunting companions. We participate in NTG hunt test and field trials with our pointer family. We have been members of the prairie pointer club, riverland pointer club, and Prairie pointer club. Dan has also served as the national pointer alliance rescue coordinator for Iowa and Nebraska and served the Spring Trial Chair for the Show Midland Pointer Club.</p>
  <p>&nbsp;&nbsp;&nbsp;&nbsp;&nbsp;We are dedicated to raising, training and breeding pointers to produce healthy dogs...</p>
</section>
<div class="abs btn read-more">Read More</div>

<div class="abs testimonials">
  <div class="box-head">TESTIMONIALS<span>&#8249; &#8250;</span></div>
  <div class="avatar" role="img" aria-label="Customer portrait" style="background:linear-gradient(#b7c4d2,#8d9aab)"></div>
  <p>"Lorem ipsum dolor sit amet,consectetuer adipiscing elit. set diem nonumy in convalis gravida neque. Nulla gravida vestibulum metis a acumsan, aliquam in sagitis ut.... "</p>
  <div class="who"><b>JOHN DOE</b>, whoever, IOWA</div>
</div>

<div class="abs news">
  <div class="box-head">LATEST NEWS &amp; EVENTS</div>
  <ul>
    <li><i role="img" aria-label="News photo" style="background:#8a8a3e"></i><span><b>January, 13th 2014.</b>Lorem ipsum dolor sit amet,consectetuer adipiscing elit.</span></li>
    <li><i role="img" aria-label="News photo" style="background:#6a3a22"></i><span><b>February, 21th 2014.</b>Lorem ipsum dolor sit amet,consectetuer adipiscing elit.</span></li>
    <li><i role="img" aria-label="News photo" style="background:#b5603a"></i><span><b>March, 11th 2014.</b>Lorem ipsum dolor sit amet,consectetuer adipiscing elit.</span></li>
    <li><i role="img" aria-label="News photo" style="background:#7a6a5a"></i><span><b>March, 28th 2014.</b>Lorem ipsum dolor sit amet,consectetuer adipiscing elit.</span></li>
    <li><i role="img" aria-label="News photo" style="background:#a0541e"></i><span><b>Avril, 09th 2014.</b>Lorem ipsum dolor sit amet,consectetuer adipiscing elit.</span></li>
    <li><i role="img" aria-label="News photo" style="background:#5e8a30"></i><span><b>Avril, 24th 2014.</b>Lorem ipsum dolor sit amet,consectetuer adipiscing elit.</span></li>
    <li><i role="img" aria-label="News photo" style="background:#3a3030"></i><span><b>May, 04th 2014.</b>Lorem ipsum dolor sit amet,consectetuer adipiscing elit.</span></li>
  </ul>
  <div class="all">View All</div>
</div>

<div class="abs footer"></div>
<div class="abs footer-head"></div>

<div class="abs fcol" style="left:150px">
  <h4>GET in Touch</h4>
  <div class="address"><b>Rustpoint, Inc.</b><br>335 - Lorem ipsum dolor 110<br>Loremipsum, IOWA, 24089<br><br>
    <table cellspacing="0" style="font-size:10px;color:#eee;line-height:12px">
      <tr><td><b>Phone</b></td><td><b>: 555 - 010 - 4420</b></td></tr>
      <tr><td><b>FAX</b></td><td>: 555 - 010 - 4428</td></tr>
      <tr><td>Email</td><td>: rp1972@mailbox.test</td></tr>
    </table>
  </div>
</div>
<div class="abs fcol" style="left:329px">
  <h4>Main menu</h4>
  <ul><li>Home</li><li>Our Dogs</li><li>Upcoming Litters</li><li>Photo Gallerys</li><li>About Us</li><li>Past Litters</li><li>Testimonials</li><li>Blog</li><li>Contact Us</li></ul>
</div>
<div class="abs fcol" style="left:440px">
  <h4>Usefull Links</h4>
  <ul><li>Help</li><li>Policy</li><li>Latest News &amp; events</li><li>Sitemap</li><li>Latest Posts</li><li>Latest Comments</li></ul>
</div>
<div class="abs fcol social" style="left:557px">
  <h4>FOLLOW US</h4>
  <ul><li><i></i>Kennelbook</li><li><i></i>Chirper</li><li><i></i>LinkedPaws</li><li><i></i>RSS</li></ul>
</div>

<div class="abs newsletter">
  <div class="box-head">Newsletter</div>
  <p>We will never share your information to any 3rd party. Receive Our updates , weekly</p>
  <div class="email">Enter your email address</div>
  <div class="btn">SUBMIT</div>
  <div class="agree"><i></i>You agree with our terms &amp; Conditions</div>
</div>

<div class="abs copyright">Copyright &copy; 2014. rustpointer.net. all rights reserved.</div>
</body>
</html>
```